Business card for a young woman who performs life enhancement activities with people who have developmental disabilities, what used to be called retardation. She wants to focus on the creative part of her work. She has a degree in art and will engage clients in art projects as well as helping them learn to do things like grocery shop, cook meals, set goals, and live independently.

Target Market(s)

Parents, caregivers, guardians, relatives of people with developmental disabilities, meaning they have not developed in their mental capacities.

Industry/Entity Type

Business

Contact Information for Business Card

Bright Harbor Services, Marisa T. Dunlop, 417 362-8094, marisa@marisadunlop.example, Life enhancement services for people with developmental disabilities. No address.

Font styles to use
Serif

Requirements
Must have
• Marisa wants it to have some indication of the art or creative part of her work with clients. But it must also be businesslike so it appeals to the parents. They have to see her as a professional, but she's compassionate and artsy. She wants just her company name on the front. The other information should be on the back.

```html
<!DOCTYPE html>
<html lang="en">
<head>
<meta charset="utf-8">
<title>Bright Harbor Services – Business Card</title>
<link rel="stylesheet" href="https://fonts.googleapis.com/css2?family=Arimo:wght@400;700&family=Lora:wght@400&family=Dancing+Script:wght@500&display=swap">
<style>
  :root {
    --canvas: #ececec;
    --card: #f3f3f3;
    --plum-deep: #5e3359;
    --plum: #86537f;
    --plum-mid: #9d6b96;
    --plum-light: #c7a6c1;
    --petal: #e6d6e3;
    --lilac: #b68ac0;
    --name: #5b1746;
    --ink: #1c1c1c;
    --tagline: #9a4b9c;
    --white: #ffffff;
  }
  * { box-sizing: border-box; margin: 0; padding: 0; }
  html, body { width: 1200px; height: 931px; overflow: hidden; }
  body {
    background: var(--canvas);
    position: relative;
    font-family: "Arimo", Arial, sans-serif;
  }
  .card {
    position: absolute;
    top: 322px;
    width: 500px;
    height: 286px;
    box-shadow: 0 6px 18px rgba(0,0,0,0.12);
    overflow: hidden;
  }

  /* Front */
  .card-front { left: 630px; }
  .front-art {
    position: absolute; inset: 0;
    background:
      radial-gradient(ellipse 22% 26% at 30% 42%, var(--petal) 0%, rgba(230,214,227,0.55) 45%, transparent 100%),
      radial-gradient(ellipse 26% 38% at 48% 18%, var(--plum-light) 0%, rgba(199,166,193,0.35) 55%, transparent 100%),
      radial-gradient(ellipse 30% 8% at 58% 82%, rgba(240,230,238,0.75) 0%, transparent 100%),
      linear-gradient(180deg, var(--plum-mid) 0%, var(--plum) 55%, var(--plum-deep) 70%, #6d3d67 100%);
  }
  .front-brand {
    position: absolute;
    right: 30px;
    top: 118px;
    display: flex;
    align-items: center;
    gap: 10px;
    font-family: "Lora", Georgia, serif;
    font-size: 27px;
    color: var(--white);
    letter-spacing: 0.3px;
  }
  .brand-dot {
    width: 14px; height: 14px;
    border-radius: 50%;
    background: var(--white);
    flex: none;
  }

  /* Back */
  .card-back { left: 70px; background: var(--card); }
  .back-brand {
    position: absolute;
    top: 46px; left: 0; width: 100%;
    display: flex;
    justify-content: center;
    align-items: center;
    gap: 9px;
    font-family: "Lora", Georgia, serif;
    font-size: 18px;
    color: var(--tagline);
  }
  .back-brand .brand-dot { width: 12px; height: 12px; background: var(--lilac); }
  .holder-name {
    position: absolute;
    top: 110px; width: 100%;
    text-align: center;
    font-weight: 700;
    font-size: 17px;
    letter-spacing: 0.4px;
    color: var(--name);
  }
  .contact {
    position: absolute;
    top: 140px; width: 100%;
    text-align: center;
    list-style: none;
    font-size: 11.5px;
    line-height: 1.45;
    color: var(--ink);
  }
  .tagline {
    position: absolute;
    left: 0; right: 0; bottom: 20px;
    text-align: center;
    font-family: "Dancing Script", cursive;
    font-size: 19px;
    color: var(--tagline);
    white-space: nowrap;
  }
</style>
</head>
<body>
  <section class="card card-back" aria-label="Business card back">
    <div class="back-brand"><span class="brand-dot"></span><span>Bright Harbor Services</span></div>
    <h1 class="holder-name">MARISA T. DUNLOP</h1>
    <ul class="contact">
      <li>417 362-8094</li>
      <li>marisa@marisadunlop.example</li>
      <li>www.brightharbor.example</li>
    </ul>
    <p class="tagline">Life enhancement services for people with developmental disabilities</p>
  </section>

  <section class="card card-front" aria-label="Business card front">
    <div class="front-art" role="img" aria-label="Hand-painted watercolour still life in plum and lilac tones: white orchids in a glass vase beside a round bowl, with a row of pale pebbles along a tabletop, showing her art practice"></div>
    <div class="front-brand"><span class="brand-dot"></span><span>Bright Harbor Services</span></div>
  </section>
</body>
</html>
```